Foldable creative restaurant menu

We require foldable restaurant menu to be placed on the each table, want it to look creative and modern with pages representing pictures of the dish not all dishes but few to represent what we do.Please get creative make sure its different, the colour should represent classy restaurant, not cheap and fast. The shape of the menu can be difference creative words must be easy to read and the logo must be in the menu here and there briefly.

Target Market(s)

Restaurant customers

Industry/Entity Type

Health And Wellness

Colors

Designer to choose colors to be used in the design.

Requirements
Must have
• foldable, must have good dish presentation pictures and must look modern and classy
Nice to have
• funky design and creative can be not just square foldable but can be interesting shape of menu.
Should not have
• boring plain spaces
• small writing
• dark pictures

```html
<!DOCTYPE html>
<html lang="en">
<head>
<meta charset="utf-8">
<title>Velora Restaurant – Table Menu</title>
<link rel="stylesheet" href="https://fonts.googleapis.com/css2?family=Lato:wght@400;700&family=Montserrat:wght@300;400&display=swap">
<style>
  :root {
    --stage: #e6e6e6;
    --paper: #f7f7f7;
    --paper-shade: #ececec;
    --ink: #1c1c1c;
    --accent: #f7953f;
    --band: #262626;
    --dish-warm: #b8682e;
    --dish-green: #7f9a3e;
    --dish-cheese: #e8c77a;
    --faded: #d4d4d4;
  }
  * { box-sizing: border-box; margin: 0; padding: 0; }
  html, body { width: 1200px; height: 1200px; overflow: hidden; }
  body {
    background: var(--stage);
    font-family: "Lato", Arial, sans-serif;
    position: relative;
  }
  .menu {
    position: absolute;
    left: 40px;
    top: 200px;
    width: 1360px;
    height: 970px;
    transform: scale(0.8235);
    transform-origin: 0 0;
    background: linear-gradient(90deg, #ffffff 0%, var(--paper) 45%, var(--paper-shade) 100%);
    overflow: hidden;
  }
  .menu-art { position: absolute; inset: 0; }
  .footer-band {
    position: absolute; left: 0; right: 0; bottom: 0; height: 43px;
    background: var(--band);
  }
  .dish-list {
    position: absolute; left: 35px; top: 0; width: 330px;
    font-size: 15.3px; line-height: 17px; color: var(--ink);
  }
  .dish { position: absolute; left: 0; width: 330px; }
  .row { position: relative; height: 17px; }
  .dish-name {
    display: flex; align-items: baseline; width: 272px; white-space: nowrap;
    color: var(--accent); text-transform: uppercase;
  }
  .dish-name .lower { text-transform: none; }
  .dish-name.plain { color: var(--ink); text-transform: none; }
  .dish-name.kids { color: var(--ink); }
  .leader { flex: 1; border-bottom: 1px dotted currentColor; margin-left: 2px; transform: translateY(-3px); }
  .price { position: absolute; top: 0; left: 295px; width: 35px; color: var(--accent); }
  .price.dark { color: var(--ink); }
  .heading { color: var(--accent); text-transform: uppercase; }
  .desc { width: 245px; }
  .brand {
    position: absolute; left: 1071px; top: 0; width: 300px; height: 270px;
    display: flex; flex-direction: column; align-items: center; justify-content: center;
    padding-top: 30px;
  }
  .brand-name {
    font-family: "Montserrat", Arial, sans-serif; font-weight: 300;
    font-size: 40px; letter-spacing: 5px; color: var(--ink);
  }
  .brand-tag {
    font-family: "Montserrat", Arial, sans-serif; font-weight: 400;
    font-size: 17px; letter-spacing: 5px; color: var(--ink); margin-top: 6px;
  }
  .partner {
    position: absolute; left: 740px; top: 872px;
    display: flex; align-items: center; gap: 8px;
    font-family: "Lato", Arial, sans-serif; font-weight: 700;
    font-size: 20px; color: var(--ink); letter-spacing: 0.5px;
  }
  .partner-dot { width: 14px; height: 14px; border-radius: 50%; background: var(--accent); }
</style>
</head>
<body>
  <main class="menu">
    <svg class="menu-art" width="1360" height="970" viewBox="0 0 1360 970">
      <defs>
        <radialGradient id="nachos-tones" cx="45%" cy="45%" r="60%">
          <stop offset="0%" stop-color="#9cae54"/>
          <stop offset="40%" stop-color="#7f9a3e"/>
          <stop offset="75%" stop-color="#b8682e"/>
          <stop offset="100%" stop-color="#8a3d1e"/>
        </radialGradient>
        <radialGradient id="parmigiana-tones" cx="35%" cy="50%" r="70%">
          <stop offset="0%" stop-color="#e8c77a"/>
          <stop offset="55%" stop-color="#d99a4c"/>
          <stop offset="100%" stop-color="#5f8a3a"/>
        </radialGradient>
        <radialGradient id="faded-salad" cx="50%" cy="50%" r="50%">
          <stop offset="0%" stop-color="#d4d4d4" stop-opacity="0.9"/>
          <stop offset="100%" stop-color="#d4d4d4" stop-opacity="0"/>
        </radialGradient>
      </defs>
      <ellipse role="img" aria-label="Faded photograph of a salad bowl" cx="470" cy="780" rx="260" ry="160" fill="url(#faded-salad)"/>
      <circle cx="862" cy="262" r="470" fill="var(--accent)"/>
      <circle role="img" aria-label="Photograph of nachos with guacamole, sour cream, coriander and fresh salsa" cx="858" cy="256" r="466" fill="url(#nachos-tones)"/>
      <circle cx="1225" cy="112" r="150" fill="var(--accent)"/>
      <circle cx="1230" cy="106" r="146" fill="#fafafa"/>
      <circle cx="1136" cy="692" r="190" fill="#ffffff" opacity="0.6"/>
      <circle cx="1136" cy="692" r="181" fill="url(#parmigiana-tones)" stroke="var(--accent)" stroke-width="9" role="img" aria-label="Photograph of chicken parmigiana with chips and green salad"/>
    </svg>

    <div class="brand">
      <div class="brand-name">Velora</div>
      <div class="brand-tag">RESTAURANT</div>
    </div>

    <div class="partner"><span class="partner-dot"></span>NORTHFIELD SPORT</div>

    <section class="dish-list">
      <div class="dish" style="top:32px">
        <div class="row"><div class="dish-name">Lamb Shank<span class="leader"></span></div><span class="price">25</span></div>
        <p class="desc">Slow cooked lamb shank served with mashed potato and vegetables (zucchini, carrot, broccoli) in tomato red wine mixed herb sauce</p>
      </div>
      <div class="dish" style="top:135px">
        <div class="heading">Roast of the Day</div>
        <div class="row"><div class="dish-name"><span class="lower">(beef or pork)</span><span class="leader"></span></div><span class="price">25</span></div>
        <p class="desc">Roasted pork or beef<br>served with mashed potato and vegetables (zucchini, carrot, broccoli) with gravy sauce (cooked with onion, celery, carrot, herb mix and red wine)</p>
      </div>
      <div class="dish" style="top:272px">
        <div class="row"><div class="dish-name">Mushroom Risotto<span class="leader"></span></div><span class="price">20</span></div>
        <p class="desc">Vegetarian mushroom risotto with Arborio rice</p>
      </div>
      <div class="dish" style="top:340px">
        <div class="row"><div class="dish-name">Pork Scallopini<span class="leader"></span></div><span class="price">23</span></div>
        <p class="desc">Medallions of pork fried in a mushroom white wine sauce with a steamed vegetables and mashed potato</p>
      </div>
      <div class="dish" style="top:426px">
        <div class="row"><div class="dish-name">Nachos<span class="leader"></span></div><span class="price">16</span></div>
        <p class="desc">Corn chips, beef, salsa, tasty cheese, grilled to perfection</p>
      </div>
      <div class="dish" style="top:494px">
        <div class="row"><div class="dish-name">Salt&nbsp;<span class="lower">and</span>&nbsp;Pepper Squid<span class="leader"></span></div><span class="price">15</span></div>
        <p class="desc">Squid, wedges with light sour cream and sweet chilli sauce</p>
      </div>
      <div class="dish" style="top:562px">
        <div class="row"><div class="dish-name">Fish&nbsp;<span class="lower">and</span>&nbsp;Chips<span class="leader"></span></div><span class="price">12</span></div>
        <p class="desc">Fish, chips, salad and tartar sauce</p>
      </div>
      <div class="dish" style="top:614px">
        <div class="heading">Sides</div>
        <div class="row"><div class="dish-name plain">Chips<span class="leader"></span></div><span class="price dark">4</span></div>
        <div class="row"><div class="dish-name plain">Garden salad<span class="leader"></span></div><span class="price dark">6</span></div>
        <div class="row"><div class="dish-name plain">Rice<span class="leader"></span></div><span class="price dark">3</span></div>
      </div>
      <div class="dish" style="top:700px">
        <div class="heading">Kid's Meal</div>
      </div>
      <div class="dish" style="top:734px">
        <div class="row"><div class="dish-name kids">Cardinale Pizza &amp; Chips<span class="leader"></span></div><span class="price dark">10</span></div>
        <p class="desc">Mozzarella cheese and Ham served with chips</p>
      </div>
      <div class="dish" style="top:802px">
        <div class="row"><div class="dish-name kids">Spaghetti Bolognese<span class="leader"></span></div><span class="price dark">7</span></div>
      </div>
      <div class="dish" style="top:825px">
        <div class="row"><div class="dish-name kids">Spaghetti&nbsp;<span class="lower">with</span>&nbsp;Meatballs<span class="leader"></span></div><span class="price dark">7</span></div>
        <div class="row"><div class="dish-name kids">Cheeseburger and Chips<span class="leader"></span></div><span class="price dark">7</span></div>
        <div class="row"><div class="dish-name kids">Fish&nbsp;<span class="lower">and</span>&nbsp;Chips<span class="leader"></span></div><span class="price dark">7</span></div>
        <div class="row"><div class="dish-name kids">Chips&nbsp;<span class="lower">and</span>&nbsp;Nuggets<span class="leader"></span></div><span class="price dark">7</span></div>
      </div>
    </section>

    <div class="footer-band"></div>
  </main>
</body>
</html>
```